KRM

I just wrote a novel that I plan on marketing through my website. Please use my uploaded files to add on to your design... The name of the book is "Lanterns under the frost".

Industry/Entity Type

Marketing

Font styles to use
Serif
Sans Serif

Colors

Designer to choose colors to be used in the design.

```html
<!DOCTYPE html>
<html lang="en">
<head>
<meta charset="utf-8">
<title>Lanterns Under the Frost — Marcus T. Ellery</title>
<link href="https://fonts.googleapis.com/css2?family=Roboto+Condensed:wght@300;400;700&family=Open+Sans:wght@400;600&display=swap" rel="stylesheet">
<style>
:root{
  --crimson:#9c1c26;
  --crimson-dark:#6e1017;
  --maroon:#7a0e17;
  --header:#5a0f14;
  --nav-active:#2b0a0c;
  --ink:#111;
  --text:#555;
  --muted:#777;
  --grey-band:#f1f1f1;
  --white:#fff;
}
*{box-sizing:border-box;margin:0;padding:0}
html,body{width:1030px;height:1200px;overflow:hidden;background:var(--white)}
body{position:relative;font-family:'Open Sans',sans-serif;color:var(--text)}
.abs{position:absolute}

/* header */
.site-header{left:0;top:0;width:1030px;height:43px;background:rgba(70,8,12,.85);z-index:2}
.site-title{left:108px;top:11px;font-family:'Roboto Condensed',sans-serif;font-weight:700;font-size:17px;color:var(--white);letter-spacing:.3px}
.nav{right:107px;top:0;display:flex;height:43px}
.nav a{font-family:'Roboto Condensed',sans-serif;font-size:16px;color:var(--white);text-decoration:none;padding:0 13px;line-height:44px}
.nav a.active{background:var(--nav-active);color:#e33b3b;padding:0 8px}

/* hero */
.hero{left:0;top:0;width:1030px;height:455px;background:radial-gradient(ellipse at 40% 50%,#b0252f 0%,var(--crimson) 55%,#84151e 100%)}
.hero-title{left:183px;top:152px;font-family:'Roboto Condensed',sans-serif;color:var(--white);font-weight:400}
.hero-title .main{font-size:70px;line-height:74px;letter-spacing:1px;display:block}
.hero-title .sub{font-size:33px;line-height:40px;margin-top:6px;display:block}
.hero-title .author{font-size:26px;letter-spacing:5px;font-weight:300;margin-top:14px;display:block}
.book{left:599px;top:77px;width:208px;height:347px;background:linear-gradient(160deg,#f1ece6 0%,#b99a8a 40%,#6d3a32 75%,#2a1513 100%);box-shadow:8px 10px 18px rgba(0,0,0,.45);border-right:6px solid #e6e6e6}
.arrow{top:212px}

/* buy bar */
.buy-bar{left:0;top:455px;width:1030px;height:46px;background:#000}
.buy-label{left:107px;top:11px;font-size:17px;color:var(--white);font-weight:400}
.stores{left:192px;top:467px;display:flex;gap:16px}
.store{height:21px;padding:0 7px;background:var(--white);border:1px solid #bbb;font-size:11px;font-weight:600;color:#222;line-height:19px;white-space:nowrap}

/* meet */
.section-heading{font-size:16.5px;color:var(--maroon);font-weight:400;text-transform:uppercase;letter-spacing:.2px}
.author-photo{left:108px;top:553px;width:152px;height:183px;background:linear-gradient(180deg,#c9d3dc 0%,#b89a86 45%,#1f2a44 100%);border:1px solid #ddd}
.bio{left:277px;top:548px;width:402px;font-size:10.5px;line-height:16.3px;color:var(--text)}
.bio p+p{margin-top:5px}
.btn{background:var(--maroon);color:var(--white);font-size:10px;border:none;display:inline-block;text-align:center}
.read-more{left:612px;top:716px;width:65px;height:21px;line-height:21px}

.mailing{left:701px;top:525px;width:222px;height:212px;background:#000;color:var(--white);padding:12px 16px}
.mailing h3{font-size:16px;font-weight:400}
.mailing .hint{font-size:11.5px;margin-top:4px}
.email-field{margin-top:10px;width:190px;height:23px;background:#3a3a3a;color:#aaa;font-size:9.5px;line-height:23px;padding-left:9px}
.signup{margin-top:10px;width:54px;height:22px;line-height:22px;font-size:9.5px}
.mailing h4{font-size:16px;font-weight:400;margin-top:12px}
.profile{display:flex;gap:8px;margin-top:6px}
.profile-pic{width:43px;height:43px;background:linear-gradient(180deg,#cfd6df,#2a3552)}
.profile-name{color:#5a78c4;font-size:12.5px}
.like-row{display:flex;align-items:center;gap:8px;margin-top:5px;font-size:9.5px;color:#bbb}
.like-btn{background:#4a63a6;color:var(--white);font-size:9.5px;font-weight:600;padding:2px 5px}

/* story band */
.story{left:0;top:762px;width:1030px;height:225px;background:var(--grey-band)}
.story-sub{left:108px;top:815px;font-size:13.5px;color:#333}
.story-sub b{color:var(--maroon);font-weight:600}
.story-text{left:108px;top:842px;width:616px;font-size:10.5px;line-height:18px;color:var(--text)}
.publisher-mark{left:753px;top:807px}

/* footer */
.footer-col h3{font-size:16.5px;font-weight:400;color:var(--maroon)}
.footer-col ul{list-style:none;margin-top:9px}
.footer-col li{font-size:10.5px;line-height:21.2px;color:var(--muted)}
.footer-col li.current{color:var(--maroon)}
.contact-line{display:flex;gap:10px;font-size:10.5px;line-height:16px;color:var(--muted)}
.pay{display:flex;flex-direction:column;gap:6px;margin-top:11px}
.card{width:32px;height:20px;border-radius:2px;font-size:7px;color:var(--white);text-align:center;line-height:20px;font-weight:600}

.bottom-bar{left:0;top:1159px;width:1030px;height:41px;background:#000}
.copyright{left:108px;top:1173px;font-size:10.5px;color:#aaa}
.social{left:757px;top:1169px;display:flex;gap:5px}
.social span{width:20px;height:20px;background:#555;color:#ddd;font-size:8px;line-height:20px;text-align:center}
.social span.first{background:#3a5a9c;color:#fff}
</style>
</head>
<body>

<section class="hero abs" aria-label="Book hero"></section>

<header class="site-header abs">
  <div class="site-title abs">LANTERNS UNDER THE FROST</div>
  <nav class="nav abs">
    <a class="active" href="#">Home</a><a href="#">Reviews</a><a href="#">About</a><a href="#">Blog</a><a href="#">Contact</a><a href="#">Links</a>
  </nav>
</header>

<svg class="arrow abs" style="left:122px" width="20" height="72" viewBox="0 0 20 72"><polyline points="17,2 3,36 17,70" fill="none" stroke="#fff" stroke-width="2"/></svg>
<svg class="arrow abs" style="left:889px" width="20" height="72" viewBox="0 0 20 72"><polyline points="3,2 17,36 3,70" fill="none" stroke="#fff" stroke-width="2"/></svg>

<h1 class="hero-title abs">
  <span class="main">LANTERNS</span>
  <span class="sub">UNDER THE FROST</span>
  <span class="author">MARCUS.T.ELLERY</span>
</h1>

<div class="book abs" role="img" aria-label="Front cover of the novel Lanterns Under the Frost"></div>

<div class="buy-bar abs">
  <div class="buy-label abs">Buy Now</div>
</div>
<div class="stores abs">
  <span class="store">Shelfwise</span>
  <span class="store">Quill &amp; Oak</span>
  <span class="store">Paperlane</span>
  <span class="store">Northbeam</span>
  <span class="store">Pagepod</span>
</div>

<h2 class="section-heading abs" style="left:108px;top:521px">Meet Marcus.T. Ellery</h2>
<div class="author-photo abs" role="img" aria-label="Portrait photo of author Marcus T. Ellery"></div>
<div class="bio abs">
  <p>Lorem ipsum dolor sit amet, consectetur adipiscing elit. Maecenas malesuada accusan odio et interdum. Donec non iaculis mauris, et commodo ante. Aliquam pulvinar nisi ut tortor vestibulum, sit amet gravida ante feugiat. Curabitur ornare, neque a elemeum egestas, purus tortor convallis nisi, at adipiscing justo mauris</p>
  <p>Fusce lacinia commodo dui, ac hendrerit dolor rutrum quis. In dolor massa, faucibus id augue ac, viverra dapibus sem. Nam ac posuere lectus, at molestie felis. Proin volutpat sit amet leo id lobortis. Vivamus vestibulum arcu ac porttitor condimentum.Proin arcu diam, dignissim nec cursus in, placerat eget dolor. Pellentesque non elit ac lacus sodales cursus. Vivamus volutpat feugiat mi id faucibus</p>
</div>
<span class="btn read-more abs">Read More</span>

<aside class="mailing abs">
  <h3>MAILING LIST</h3>
  <div class="hint">Sign up for email updates:</div>
  <div class="email-field">Enter your e-mail address</div>
  <div class="btn signup">SIGN UP</div>
  <h4>Find Marcus Online</h4>
  <div class="profile">
    <div class="profile-pic" role="img" aria-label="Small author profile photo"></div>
    <div>
      <div class="profile-name">Marcus T.Ellery</div>
      <div class="like-row"><span class="like-btn">Like</span>125 Peole like</div>
    </div>
  </div>
</aside>

<section class="story abs"></section>
<h2 class="section-heading abs" style="left:108px;top:783px">Lanterns Under the Frost</h2>
<div class="story-sub abs">A story Of <b>Money Murder, Sex and Family</b> ties in the hear of the city.</div>
<div class="story-text abs">
  Read along as Marcus T.Ellery Masterfully paint this Harbor Vale tale like no other -The M.O.B. boys" clash in a rain bullets against north side own "yaho boys.<br>
  Lorem ipsum dolor sit amet, consectetur adipiscing elit. Etiam rhoncus lacus vel sapien rutr sit amet pellentesque ipsum imperdiet. Vestibulum a dignissim lacus. Donec ac euismod eros. Aenean pharetra lorem at suscipit malesuada.Donec adicing odio ac libero viverra, ut consequat diam hendrerit. Quisque intedum massa sit amet sem condiment aliquet eget in tortor. Duis odio urna, faucibus vel adipiscing quis, varius fermentum tellus. Quisque quis vestibulum nibhaecenas eu tempor magna. Aliquam at dapibus nisi.
</div>
<svg class="publisher-mark abs" width="160" height="160" viewBox="0 0 160 160" role="img" aria-label="KRM publisher mark">
  <circle cx="80" cy="80" r="79" fill="#111"/>
  <text x="80" y="92" text-anchor="middle" font-family="Open Sans, sans-serif" font-size="36" font-weight="600" fill="#fff">KRM</text>
</svg>

<div class="footer-col abs" style="left:108px;top:1006px">
  <h3>The Website</h3>
  <ul><li class="current">Home Page</li><li>Contact Information</li><li>Marcus Ellery Biography</li><li>Interview with Marcus Ellery</li><li>Frequently Asked Questions</li></ul>
</div>
<div class="footer-col abs" style="left:338px;top:1006px">
  <h3>The News</h3>
  <ul><li>Novel</li><li>Recent News</li><li>Marcus Ellery Blog</li><li>Follow Marcus on Chirpa</li><li>Upcoming Events</li></ul>
</div>
<div class="footer-col abs" style="left:528px;top:1006px">
  <h3>Contact</h3>
  <div class="contact-line" style="margin-top:9px">
    <svg width="16" height="18" viewBox="0 0 16 18"><path d="M8 1a5 5 0 0 0-5 5c0 4 5 9 5 9s5-5 5-9a5 5 0 0 0-5-5z" fill="none" stroke="#7a0e17" stroke-width="1.5"/><circle cx="8" cy="6" r="1.8" fill="#7a0e17"/><path d="M1 17h14" stroke="#7a0e17" stroke-width="1.5"/></svg>
    <span>Marcus Ellery PO Box 48120<br>Harbor Vale</span>
  </div>
  <div class="contact-line" style="margin-top:17px">
    <svg width="16" height="16" viewBox="0 0 16 16"><path d="M9 2C6 3 5 6 5 8s1 5 4 6" fill="none" stroke="#7a0e17" stroke-width="2.5" stroke-linecap="round"/></svg>
    <span>Phone: +555 014 2287</span>
  </div>
  <div class="contact-line" style="margin-top:17px">
    <svg width="16" height="16" viewBox="0 0 16 16"><rect x="1.5" y="4" width="13" height="9" fill="none" stroke="#7a0e17" stroke-width="1.2"/><polyline points="1.5,4 8,9 14.5,4" fill="none" stroke="#7a0e17" stroke-width="1.2"/></svg>
    <span>Email: lanternsfrost@inkpost.net</span>
  </div>
</div>
<div class="footer-col abs" style="left:853px;top:1006px">
  <h3>Payment</h3>
  <div class="pay">
    <span class="card" style="background:#2a7ac6">Axio</span>
    <span class="card" style="background:#2b3a8c">Vero</span>
    <span class="card" style="background:#b86a2a">Dalo</span>
    <span class="card" style="background:#c0392b">Mira</span>
  </div>
</div>

<footer class="bottom-bar abs"></footer>
<div class="copyright abs">Copyright © 2014 lanternsunderthefrost . All Rights Reserved.</div>
<div class="social abs">
  <span class="first">Kn</span><span>Ch</span><span>Pl</span><span>Pn</span><span>Vu</span><span>Fd</span><span>Wk</span>
</div>

</body>
</html>
```